Wageline Associates Business Card Design

We need a business card designed around our new logo. The business card should be modern in design & should communicate success, confidence, power, sophistication. The target market is young business professionals. This is for a human resource & payroll outsourcing business.

```html
<!DOCTYPE html>
<html lang="en">
<head>
<meta charset="UTF-8">
<title>Wageline Associates Business Card</title>
<link href="https://fonts.googleapis.com/css2?family=Roboto:wght@400;500&display=swap" rel="stylesheet">
<style>
  :root {
    --page-bg: #e6e6e6;
    --card-bg: #ffffff;
    --ink: #111111;
    --text-grey: #3c3c3c;
    --rule-grey: #8a8a8a;
    --brand-red: #c4222b;
    --band-black: #050505;
  }
  * { margin: 0; padding: 0; box-sizing: border-box; }
  html, body { width: 1200px; height: 800px; overflow: hidden; }
  body {
    background: var(--page-bg);
    font-family: "Roboto", Arial, sans-serif;
    position: relative;
  }
  .card {
    position: absolute;
    left: 80px;
    top: 106px;
    width: 1040px;
    height: 588px;
    background: var(--card-bg);
    box-shadow: 0 8px 24px rgba(0,0,0,0.18);
    overflow: hidden;
  }
  .brand {
    position: absolute;
    right: 68px;
    top: 78px;
    display: flex;
    align-items: center;
    gap: 14px;
  }
  .brand-dot {
    width: 22px; height: 22px;
    border-radius: 50%;
    background: var(--brand-red);
  }
  .brand-name {
    font-size: 44px;
    font-weight: 500;
    color: var(--ink);
    letter-spacing: 0.5px;
  }
  .holder {
    position: absolute;
    left: 62px;
    top: 290px;
  }
  .holder-name {
    font-size: 37px;
    font-weight: 500;
    color: var(--ink);
    line-height: 1.1;
  }
  .holder-title {
    font-size: 26px;
    font-weight: 400;
    color: var(--brand-red);
    line-height: 1.2;
  }
  .divider {
    position: absolute;
    left: 62px;
    right: 62px;
    top: 379px;
    height: 2px;
    background: var(--rule-grey);
  }
  .contacts {
    position: absolute;
    left: 62px;
    top: 398px;
    list-style: none;
  }
  .contacts li {
    display: flex;
    align-items: center;
    height: 33px;
    font-size: 24px;
    color: var(--text-grey);
  }
  .contacts svg {
    width: 24px; height: 24px;
    margin-right: 19px;
    fill: var(--ink);
    flex-shrink: 0;
  }
  .address {
    position: absolute;
    right: 58px;
    top: 434px;
    text-align: right;
    font-style: normal;
    font-size: 24px;
    line-height: 32px;
    color: var(--text-grey);
  }
  .band {
    position: absolute;
    left: 0; bottom: 0;
    width: 1040px; height: 18px;
  }
</style>
</head>
<body>
  <div class="card">
    <div class="brand">
      <span class="brand-dot"></span>
      <span class="brand-name">Wageline Associates</span>
    </div>

    <div class="holder">
      <div class="holder-name">Daniel Hale</div>
      <div class="holder-title">President</div>
    </div>

    <div class="divider"></div>

    <ul class="contacts">
      <li>
        <svg viewBox="0 0 24 24" aria-hidden="true"><path d="M6.6 10.8c1.4 2.8 3.8 5.1 6.6 6.6l2.2-2.2c.3-.3.7-.4 1-.2 1.1.4 2.3.6 3.6.6.6 0 1 .4 1 1V20c0 .6-.4 1-1 1C10.6 21 3 13.4 3 4c0-.6.4-1 1-1h3.5c.6 0 1 .4 1 1 0 1.3.2 2.5.6 3.6.1.3 0 .7-.2 1L6.6 10.8z"/></svg>
        555-214-7730
      </li>
      <li>
        <svg viewBox="0 0 24 24" aria-hidden="true"><path d="M7 1h10c1.1 0 2 .9 2 2v18c0 1.1-.9 2-2 2H7c-1.1 0-2-.9-2-2V3c0-1.1.9-2 2-2zm0 3v15h10V4H7z"/></svg>
        555-382-6104
      </li>
      <li>
        <svg viewBox="0 0 24 24" aria-hidden="true"><path d="M7 3h8l2 2v4H7V3zm-4 7h18c.6 0 1 .4 1 1v9c0 .6-.4 1-1 1H3c-.6 0-1-.4-1-1v-9c0-.6.4-1 1-1zm3 3v2h12v-2H6z"/></svg>
        555-469-2851
      </li>
      <li>
        <svg viewBox="0 0 24 24" aria-hidden="true"><path d="M2 5h20v14H2V5zm2 2.2V17h16V7.2l-8 5.6-8-5.6zM5.5 7l6.5 4.5L18.5 7h-13z"/></svg>
        name@wageline.com
      </li>
    </ul>

    <address class="address">
      4120 Larkspur Court<br>
      Fairview, Oregon 97024<br>
      www.wageline.com
    </address>

    <svg class="band" viewBox="0 0 1040 18" preserveAspectRatio="none" aria-hidden="true">
      <polygon points="0,0 598,0 592,18 0,18" fill="var(--band-black)"/>
      <polygon points="603,0 1040,0 1040,18 597,18" fill="var(--brand-red)"/>
    </svg>
  </div>
</body>
</html>
```